Business Card Design Project

I am seeking a business card for my life coaching career. I specialize in coaching executives and entrepreneurs. Consciousness plays a key role in my practice.
Updates

I would like to see different fonts -I don't like the way the capital J looks. I only want my name once on the card, on the front. I like everything centered on the front, with a white background, grey and green on the front; and the same grey on the back with bullet points next to each quality; centered. I like a subtle shadow of the mountains behind the text on the back of the card. I don't want the mountains on either side to be too big. Thank you.

Target Market(s)

Middle age business owners/executives

Industry/Entity Type

Business

Contact Information for Business Card

The front design is my name and a mountain logo. I want to have my name prominently shown.

Requirements
Must have
• Front of card:
• My name prominent sized font
• Helping clients lead more fulfilling lives;
• Executive Life Coach
• 555-304-7781
• rkovet4@mailbriar.com
• Back of Card:
• Providing Unparalleled support
• Providing a safe place to grow in self-awareness
• 20+ years entrepreneurial experience
• Trust
• Integrity
Nice to have
• Easy to read font; warm colors reflecting a masculine personality.

Files

```html
<!DOCTYPE html>
<html lang="en">
<head>
<meta charset="UTF-8">
<title>Executive Life Coach – Card Back</title>
<link rel="stylesheet" href="https://fonts.googleapis.com/css2?family=Amaranth&display=swap">
<style>
  :root {
    --canvas-bg: #ffffff;
    --card-grey: #4a4646;
    --card-edge: #2c2a2a;
    --text-light: #f6f4f2;
  }
  html, body {
    margin: 0;
    padding: 0;
    width: 1200px;
    height: 1000px;
    overflow: hidden;
    background: var(--canvas-bg);
  }
  .canvas {
    position: relative;
    width: 1200px;
    height: 1000px;
  }
  .card-back {
    position: absolute;
    left: 75px;
    top: 200px;
    width: 1050px;
    height: 599px;
    background: var(--card-grey);
    border: 1px solid var(--card-edge);
  }
  .qualities {
    position: absolute;
    left: 145px;
    top: 258px;
    margin: 0;
    padding: 0;
    list-style: none;
    font-family: "Amaranth", sans-serif;
    font-size: 37px;
    line-height: 47.5px;
    color: var(--text-light);
  }
  .qualities li {
    position: relative;
    padding-left: 36px;
    white-space: nowrap;
  }
  .qualities li::before {
    content: "";
    position: absolute;
    left: 0;
    top: 22px;
    width: 9px;
    height: 4px;
    background: var(--text-light);
  }
  .qualities li::after {
    content: "";
    position: absolute;
    left: 8px;
    top: 18px;
    border-left: 7px solid var(--text-light);
    border-top: 6px solid transparent;
    border-bottom: 6px solid transparent;
  }
</style>
</head>
<body>
  <div class="canvas">
    <section class="card-back">
      <ul class="qualities">
        <li>Providing Unparalleled support</li>
        <li>Providing a safe place to grow in self-awareness</li>
        <li>20+ years of entrepreneurial experience</li>
        <li>Trust</li>
        <li>Integrity</li>
      </ul>
    </section>
  </div>
</body>
</html>
```